Hairdressing Supplier 4 Page Specials Leaflet

A 4 page flyer for our sales reps and stores to hand out. Fresh and relevant design required based on past samples attached.
The flyer features around 30 - 50 products that show a photo, the name of the product and a price. A basic task, but those chosen will show the extra flair required.
Old examples of our flyers are attached. My favourite is 2014 0203.pdf
Full instructions and photos can be downloaded from here:
https://www.filquarry.net/sh/kemrotu84c317wq/BBQmLo7tyn2-h8J-_PeRdWsvzk
Updates
Please note I have updated the word document file from the folder to include one more product - page 1 section 4.
I will update link in the main project but please see new link below:
Target Market(s)
salon owners
women 20-50
Industry/Entity Type
Product

```html
<!DOCTYPE html>
<html lang="en">
<head>
<meta charset="utf-8">
<title>VELO – New Year New Salon Specials</title>
<link rel="stylesheet" href="https://fonts.googleapis.com/css2?family=Lato:wght@300;400;700;900&family=Oswald:wght@500;700&family=Libre+Franklin:wght@900&display=swap">
<style>
  :root {
    --stage: #e4e4e4;
    --red: #d3202a;
    --red-dark: #a8141c;
    --purple-dark: #3b2570;
    --purple-light: #8a6cc6;
    --silver-1: #f7f7f7;
    --silver-2: #dadada;
    --copper-1: #8e2f12;
    --copper-2: #c8582a;
    --copper-3: #e48a4c;
    --ink: #2a2a2a;
    --line: #8a8aa8;
    --white: #ffffff;
  }
  * { box-sizing: border-box; margin: 0; padding: 0; }
  html, body { width: 928px; height: 1200px; overflow: hidden; background: var(--stage); }
  .flyer {
    position: absolute; left: 46px; top: 18px;
    width: 836px; height: 1164px; overflow: hidden;
    background: linear-gradient(160deg, var(--silver-1), var(--silver-2));
    font-family: "Lato", sans-serif; color: var(--ink);
  }
  .flyer-art { position: absolute; inset: 0; }

  .brand-tab {
    position: absolute; left: 26px; top: 0; width: 309px; height: 224px;
    background: var(--red); border-radius: 0 0 22px 22px;
    display: flex; align-items: center; justify-content: center;
    box-shadow: 0 4px 10px rgba(0,0,0,.25);
  }
  .brand-name {
    font-family: "Lato", sans-serif; font-weight: 300; font-size: 92px;
    color: var(--white); letter-spacing: 4px; line-height: 1;
  }

  .store-bar {
    position: absolute; left: 353px; top: 50px; width: 483px; height: 77px;
    background: var(--purple-light); border-radius: 38px 0 0 38px;
    color: var(--white); font-size: 9.5px; line-height: 11.5px;
  }
  .store { position: absolute; top: 8px; }
  .store strong { font-weight: 900; font-size: 10.5px; display: block; }
  .store--1 { left: 19px; } .store--2 { left: 139px; } .store--3 { left: 248px; } .store--4 { left: 368px; }
  .store-contact { position: absolute; right: 14px; font-size: 9.5px; white-space: nowrap; display: flex; gap: 8px; align-items: center; }
  .store-contact--phones { top: 52px; }
  .store-contact--web { top: 64px; }
  .icon { width: 9px; height: 9px; vertical-align: -1px; margin-right: 3px; }

  .headline { position: absolute; color: var(--white); font-family: "Oswald", sans-serif; font-weight: 700; text-transform: uppercase; line-height: 1; text-shadow: 0 2px 6px rgba(0,0,0,.3); }
  .headline--main { left: 40px; top: 398px; font-size: 80px; }
  .headline--sub { left: 92px; top: 480px; font-size: 42px; font-weight: 500; }

  .offer { position: absolute; left: 26px; font-family: "Libre Franklin", sans-serif; font-weight: 900; font-size: 66px; line-height: 1; letter-spacing: -1px; }
  .offer--top { top: 766px; color: var(--purple-dark); }
  .offer--bottom { top: 834px; color: var(--purple-light); }

  .sales-title {
    position: absolute; left: 490px; top: 857px; width: 346px; height: 40px;
    background: var(--red); border-radius: 20px 0 0 20px;
    color: var(--white); font-weight: 700; font-size: 21px;
    display: flex; align-items: center; padding-left: 18px;
  }
  .sales-team { position: absolute; left: 487px; top: 905px; font-size: 12.5px; line-height: 15.5px; }
  .sales-row { position: relative; height: 15.5px; white-space: nowrap; }
  .sales-row span { position: absolute; top: 0; }
  .sales-region { left: 0; }
  .sales-rep { left: 111px; }
  .sales-phone { left: 223px; }

  .badge-text {
    position: absolute; width: 100px; text-align: center;
    color: var(--white); font-weight: 700; font-size: 15px; line-height: 17px;
  }
  .price-badge { position: absolute; left: 405px; top: 1065px; width: 100px; text-align: center; color: var(--white); font-family: "Oswald", sans-serif; font-weight: 700; line-height: 1; }
  .price-badge .price { font-size: 27px; display: block; }
  .price-badge .save { font-size: 15px; display: block; margin-top: 2px; }
</style>
</head>
<body>
<main class="flyer">
  <svg class="flyer-art" width="836" height="1164" viewBox="0 0 836 1164" xmlns="http://www.w3.org/2000/svg">
    <defs>
      <linearGradient id="hair-tones" x1="0" y1="0" x2="1" y2="1">
        <stop offset="0" stop-color="#c8582a"/>
        <stop offset=".45" stop-color="#e48a4c"/>
        <stop offset="1" stop-color="#8e2f12"/>
      </linearGradient>
      <radialGradient id="product-well" cx=".5" cy=".45" r=".6">
        <stop offset="0" stop-color="#ffffff"/>
        <stop offset="1" stop-color="#e6e0f0"/>
      </radialGradient>
      <polygon id="burst" points="50,0 42.2,8.4 46.2,19.1 35.8,23.9 35.4,35.4 23.9,35.8 19.1,46.2 8.4,42.2 0,50 -8.4,42.2 -19.1,46.2 -23.9,35.8 -35.4,35.4 -35.8,23.9 -46.2,19.1 -42.2,8.4 -50,0 -42.2,-8.4 -46.2,-19.1 -35.8,-23.9 -35.4,-35.4 -23.9,-35.8 -19.1,-46.2 -8.4,-42.2 0,-50 8.4,-42.2 19.1,-46.2 23.9,-35.8 35.4,-35.4 35.8,-23.9 46.2,-19.1 42.2,-8.4"/>
    </defs>

    <rect role="img" aria-label="Photo of a woman with long glossy copper-red hair, eyes closed" x="0" y="110" width="836" height="690" fill="url(#hair-tones)"/>

    <path d="M0,0 H836 V140 C640,150 300,230 0,318 Z" fill="var(--silver-1)"/>
    <path d="M0,300 C300,214 640,132 836,124 V158 C640,170 300,246 0,322 Z" fill="var(--purple-dark)"/>
    <path d="M0,318 C300,230 640,150 836,140 V146 C640,156 300,238 0,324 Z" fill="var(--white)"/>

    <path d="M0,668 C250,618 520,680 836,762 V796 C520,712 250,652 0,690 Z" fill="var(--purple-dark)"/>
    <path d="M0,690 C250,652 520,712 836,796 V1164 H0 Z" fill="var(--silver-1)"/>

    <g class="product-circle">
      <circle cx="160" cy="633" r="106" fill="var(--purple-dark)"/>
      <circle cx="160" cy="633" r="94" fill="var(--purple-light)"/>
      <circle cx="160" cy="633" r="89" fill="url(#product-well)"/>
      <rect role="img" aria-label="Shampoo pump bottle" x="126" y="558" width="64" height="146" rx="10" fill="#c9b6e4"/>
    </g>
    <g class="product-circle">
      <circle cx="375" cy="672" r="87" fill="var(--purple-dark)"/>
      <circle cx="375" cy="672" r="76" fill="var(--purple-light)"/>
      <circle cx="375" cy="672" r="71" fill="url(#product-well)"/>
      <ellipse role="img" aria-label="Tubs of hair wax" cx="375" cy="672" rx="48" ry="36" fill="#e63fa8"/>
    </g>
    <g class="product-circle">
      <circle cx="580" cy="745" r="80" fill="var(--purple-dark)"/>
      <circle cx="580" cy="745" r="69" fill="var(--purple-light)"/>
      <circle cx="580" cy="745" r="64" fill="url(#product-well)"/>
      <rect role="img" aria-label="Spray bottle of leave-in treatment" x="563" y="690" width="34" height="104" rx="6" fill="#4fb8b8"/>
    </g>

    <!-- bottom red wave, kept below the sales list and products -->
    <path d="M0,1150 C260,1140 560,1115 836,1078 V1164 H0 Z" fill="var(--red)"/>
    <path d="M0,1145 C260,1135 560,1110 836,1073 V1078 C560,1115 260,1140 0,1150 Z" fill="var(--red-dark)"/>

    <rect role="img" aria-label="Row of red shampoo and conditioner bottles" x="26" y="926" width="151" height="103" rx="8" fill="#c8161d"/>
    <rect role="img" aria-label="Red tub of hair treatment masque" x="215" y="940" width="101" height="90" rx="6" fill="#c41a1f"/>
    <rect role="img" aria-label="Red tube of hair treatment" x="50" y="1045" width="43" height="88" rx="5" fill="#b0131a"/>
    <rect role="img" aria-label="White bottle of peroxide developer" x="173" y="1042" width="43" height="90" rx="7" fill="#f4f4f4" stroke="#9aa3b8"/>
    <rect role="img" aria-label="Cordless hair clippers" x="311" y="1046" width="88" height="72" rx="14" fill="#e9e9e9" stroke="#b5b5b5"/>

    <use href="#burst" transform="translate(336,943)" fill="var(--purple-dark)"/>
    <use href="#burst" transform="translate(160,995) scale(.96)" fill="var(--purple-dark)"/>
    <use href="#burst" transform="translate(115,1086) scale(.9)" fill="var(--purple-dark)"/>
    <use href="#burst" transform="translate(250,1086) scale(.9)" fill="var(--purple-dark)"/>
    <use href="#burst" transform="translate(455,1093) scale(1.0)" fill="var(--purple-dark)"/>

    <g stroke="var(--line)" stroke-width="1" fill="none">
      <path d="M567,913 H594"/>
      <path d="M516,928.5 H584 V959.5 H568 M584,944 H594"/>
      <path d="M572,975 H588 V990.5 H560 M588,975 H594"/>
      <path d="M538,1021.5 H594"/>
      <path d="M515,1037 H594"/>
      <path d="M558,1052.5 H594"/>
    </g>
  </svg>

  <div class="brand-tab"><span class="brand-name">VELO</span></div>

  <section class="store-bar">
    <div class="store store--1"><strong>Northgate Superstore</strong>Unit 3, 27 Harlow Road<br>NORTHGATE<br>NSW 2770</div>
    <div class="store store--2"><strong>Eastwood Superstore</strong>412 The Kestrel Drive<br>EASTWOOD NSW 2164</div>
    <div class="store store--3"><strong>Hillview Pick &amp; Pay</strong>18 Wattle Place<br>HILLVIEW NSW 2147</div>
    <div class="store store--4"><strong>All Correspondence:</strong>PO Box 46<br>EASTFIELD NSW 2760</div>
    <div class="store-contact store-contact--phones">
      <span><svg class="icon" viewBox="0 0 10 10"><rect width="10" height="10" rx="2" fill="#fff"/><path d="M3 2.5 L4 4 L3.5 5 Q4.5 6.5 5 6.5 L6 6 L7.5 7 L7 8 Q3 8 2 3 Z" fill="#8a6cc6"/></svg>+61 2 9400 1120</span>
      <span><svg class="icon" viewBox="0 0 10 10"><rect width="10" height="10" rx="2" fill="#fff"/><path d="M3 2.5 L4 4 L3.5 5 Q4.5 6.5 5 6.5 L6 6 L7.5 7 L7 8 Q3 8 2 3 Z" fill="#8a6cc6"/></svg>+61 2 9400 1135</span>
      <span><svg class="icon" viewBox="0 0 10 10"><rect y="2" width="10" height="7" fill="#fff"/><path d="M0 2 L5 6 L10 2" stroke="#8a6cc6" fill="none"/></svg>info@corvane.com.au</span>
    </div>
    <div class="store-contact store-contact--web">
      <span><svg class="icon" viewBox="0 0 10 10"><circle cx="5" cy="5" r="4.5" fill="none" stroke="#fff"/><path d="M0.5 5 H9.5 M5 0.5 V9.5" stroke="#fff"/></svg>www.corvane.com.au ABN: 51 204 337 918</span>
    </div>
  </section>

  <h1 class="headline headline--main">New Year</h1>
  <p class="headline headline--sub">New Salon</p>

  <h2 class="offer offer--top">All Treatments</h2>
  <p class="offer offer--bottom">Reduced</p>

  <span class="badge-text" style="left:286px; top:926px;">Prize<br>Reduced</span>
  <span class="badge-text" style="left:110px; top:978px;">Prize<br>Reduced</span>
  <span class="badge-text" style="left:65px; top:1069px;">Prize<br>Reduced</span>
  <span class="badge-text" style="left:200px; top:1069px;">Prize<br>Reduced</span>
  <div class="price-badge"><span class="price">$139</span><span class="save">SAVE $49</span></div>

  <h3 class="sales-title">Order from our sales team:</h3>
  <div class="sales-team">
    <div class="sales-row"><span class="sales-region">Sydney Metro</span><span class="sales-rep">Marc Devane</span><span class="sales-phone">0400 512 300</span></div>
    <div class="sales-row"><span class="sales-region">ACT</span></div>
    <div class="sales-row"><span class="sales-region">Sydney West</span><span class="sales-rep">Peter Rowan</span><span class="sales-phone">0400 512 300</span></div>
    <div class="sales-row"><span class="sales-region">Sydney North</span></div>
    <div class="sales-row"><span class="sales-region">Central Coast</span><span class="sales-rep">Head Office</span><span class="sales-phone">02 9400 1120</span></div>
    <div class="sales-row"><span class="sales-region">North Coast</span></div>
    <div class="sales-row"><span class="sales-region">SE QLD</span><span class="sales-rep">Cody Marsh</span><span class="sales-phone">0400 512 050</span></div>
    <div class="sales-row"><span class="sales-region">VIC</span><span class="sales-rep">Ruth Holland</span><span class="sales-phone">0400 318 963</span></div>
    <div class="sales-row"><span class="sales-region">NSW Colour</span><span class="sales-rep">Specialist Nina</span><span class="sales-phone">0400 670 144</span></div>
    <div class="sales-row"><span class="sales-rep">Carrow (syd Metro)</span></div>
  </div>
</main>
</body>
</html>
```